Business Card Design Project

Company name will be Tallow Crest (named after my black lab and his fraying muzzle) Business is in the body armor, Security product industry servicing the state, local, and federal law enforcement markets. I want a more formal and serious logo for both business cards and letterhead

```html
<!DOCTYPE html>
<html lang="en">
<head>
<meta charset="utf-8">
<title>Tallow Crest – Business Card</title>
<link rel="stylesheet" href="https://fonts.googleapis.com/css2?family=Nunito+Sans:wght@300;600;800&display=swap">
<style>
  :root {
    --backdrop: #7d766c;
    --card: #1e1412;
    --card-edge: #3a2d29;
    --logo: #f4f4f2;
    --name: #ffffff;
    --title-red: #c8221e;
    --contact: #d6d2cf;
  }
  * { box-sizing: border-box; margin: 0; padding: 0; }
  html, body {
    width: 1200px;
    height: 803px;
    overflow: hidden;
    background: var(--backdrop);
    font-family: "Nunito Sans", Arial, sans-serif;
  }
  .canvas {
    position: relative;
    width: 1200px;
    height: 803px;
  }
  .card {
    position: absolute;
    width: 655px;
    height: 376px;
    background: var(--card);
    border: 1px solid var(--card-edge);
  }
  .card--front { left: 52px; top: 81px; }
  .card--back  { left: 427px; top: 340px; }

  .wordmark {
    position: absolute;
    left: 0;
    width: 100%;
    text-align: center;
    font-weight: 800;
    font-size: 50px;
    letter-spacing: -1px;
    line-height: 1;
    color: var(--logo);
    white-space: nowrap;
  }
  .card--front .wordmark { top: 143px; }
  .card--back .wordmark  { top: 80px; }

  .holder {
    position: absolute;
    left: 0;
    width: 100%;
    text-align: center;
  }
  .holder__name {
    top: 187px;
    font-weight: 600;
    font-size: 21px;
    letter-spacing: 1px;
    color: var(--name);
  }
  .holder__title {
    top: 220px;
    font-weight: 800;
    font-size: 15px;
    letter-spacing: 0.5px;
    color: var(--title-red);
  }

  .contact {
    position: absolute;
    top: 298px;
    font-weight: 300;
    font-size: 15px;
    line-height: 22px;
    color: var(--contact);
    letter-spacing: 0.3px;
  }
  .contact--direct { left: 114px; }
  .contact--address { right: 113px; text-align: right; }
</style>
</head>
<body>
  <main class="canvas">
    <section class="card card--front" aria-label="Card front">
      <div class="wordmark">TALLOW CREST</div>
    </section>

    <section class="card card--back" aria-label="Card back">
      <div class="wordmark">TALLOW CREST</div>
      <p class="holder holder__name">CARL WESTON</p>
      <p class="holder holder__title">REP PRINCIPAL</p>
      <p class="contact contact--direct">cweston@tallowcrest.com<br>555-204-7316</p>
      <p class="contact contact--address">1470 HARBOR LANE NORTH<br>PORT ALDEN, FL 32901</p>
    </section>
  </main>
</body>
</html>
```